Email Signiture and letterhead design

we are looking for a modern business design to incorporate our logo and iso certification plus social icons for Twitter, LinkedIn, and youtube
they must include our UK vat and also company registration as text but I can fill these out. Email signature to have a link/icon to our webshop www.dremlox.co.uk

Target Market(s)

All

Font styles to use
Serif
Sans Serif

Requirements
Must have
• Address, tel, email , web details incorperated
Nice to have
• a professional looking letter head and email signiture, Email signature to have a link/icon to our webshop www.dremlox.co.uk

```html
<!DOCTYPE html>
<html lang="en">
<head>
<meta charset="utf-8">
<title>Dremlox Hubs &amp; Bearings Ltd – Letterhead and Email Signature</title>
<link rel="stylesheet" href="https://fonts.googleapis.com/css2?family=Montserrat:wght@400;500;600;700&family=Questrial&display=swap">
<style>
  :root {
    --brand-red: #e31e24;
    --ink: #2b2b2b;
    --body-grey: #6d6e71;
    --paper: #ffffff;
    --backdrop: #e4e5e7;
    --shadow: rgba(0, 0, 0, 0.18);
    --signature-fill: #ececee;
  }
  * { margin: 0; padding: 0; box-sizing: border-box; }
  html, body { width: 1200px; height: 898px; overflow: hidden; }
  body {
    background: var(--backdrop);
    font-family: "Montserrat", sans-serif;
    color: var(--ink);
    position: relative;
  }

  /* ---------- Letterhead ---------- */
  .letterhead {
    position: absolute; left: 50px; top: 69px;
    width: 541px; height: 760px;
    background: var(--paper);
    box-shadow: 4px 4px 10px var(--shadow);
  }
  .brand {
    position: absolute; display: flex; align-items: center; gap: 7px;
    color: var(--brand-red); font-weight: 700; white-space: nowrap;
  }
  .brand-mark { display: block; background: var(--brand-red); border-radius: 50%; }
  .letterhead .brand { left: 22px; top: 58px; font-size: 15px; letter-spacing: 0.2px; }
  .letterhead .brand-mark { width: 14px; height: 14px; }

  .company-address {
    position: absolute; right: 37px; top: 47px;
    text-align: right; font-size: 9.5px; line-height: 12.3px; color: var(--ink);
  }
  .company-address .pin { position: absolute; right: -13px; top: 0; }

  .recipient { position: absolute; left: 25px; top: 150px; }
  .recipient-name {
    color: var(--brand-red); font-weight: 600; font-size: 18px;
    letter-spacing: 0.3px; margin-bottom: 7px;
  }
  .recipient p { font-size: 10px; line-height: 12.8px; margin-bottom: 4.5px; }
  .recipient p.recipient-address { margin-bottom: 0; }

  .letter-date {
    position: absolute; right: 25px; top: 223px;
    font-size: 11px; font-weight: 600; letter-spacing: 0.2px;
  }

  .letter-body {
    position: absolute; left: 22px; top: 260px; width: 473px;
    font-family: "Questrial", sans-serif; font-size: 10.3px; line-height: 12.5px;
    color: var(--body-grey); text-align: justify;
  }
  .letter-body p + p { margin-top: 12.5px; }
  .letter-body p.tight { margin-top: 0; }
  .letter-body p.spaced { margin-top: 25px; }

  .sign-off {
    position: absolute; left: 40px; top: 511px;
    font-family: "Questrial", sans-serif; font-size: 14.5px; color: var(--ink);
  }
  .handwritten-signature {
    position: absolute; left: 50px; top: 542px; width: 104px; height: 64px;
    background: var(--signature-fill); border-radius: 4px;
  }

  .letter-footer { position: absolute; left: 28px; top: 705px; list-style: none; }
  .letter-footer li {
    display: flex; align-items: center; gap: 4px;
    font-size: 9.5px; line-height: 12.5px; color: var(--ink);
  }

  .contact-icon { flex: none; }

  /* ---------- Email signature ---------- */
  .email-signature {
    position: absolute; left: 610px; top: 381px;
    width: 540px; height: 137px;
    background: var(--paper);
    box-shadow: 4px 4px 10px var(--shadow);
  }
  .email-signature .brand { left: 14px; top: 46px; font-size: 12px; gap: 5px; }
  .email-signature .brand-mark { width: 11px; height: 11px; }

  .sender { position: absolute; left: 14px; top: 73px; }
  .sender-name { color: var(--brand-red); font-weight: 700; font-size: 13px; }
  .sender-role { font-size: 6.8px; margin-top: 1px; }

  .sender-contacts, .sender-address {
    position: absolute; top: 101px; list-style: none;
    font-size: 6.6px; line-height: 9.2px; color: var(--ink);
  }
  .sender-contacts { left: 14px; }
  .sender-contacts li { display: flex; align-items: center; gap: 2px; }
  .sender-address { left: 91px; }

  .social { position: absolute; left: 187px; top: 101px; text-align: center; }
  .social-title { font-size: 6.2px; font-weight: 600; margin-bottom: 4px; }
  .social-links { display: flex; gap: 3px; list-style: none; }
  .social-links li {
    width: 14px; height: 14px; border-radius: 50%; background: var(--brand-red);
  }
</style>
</head>
<body>

<article class="letterhead">
  <div class="brand"><span class="brand-mark"></span>Dremlox Hubs &amp; Bearings Ltd</div>

  <address class="company-address">
    <svg class="pin" width="9" height="12" viewBox="0 0 9 12" aria-hidden="true">
      <path d="M4.5 0C2 0 0 2 0 4.4 0 7.6 4.5 12 4.5 12S9 7.6 9 4.4C9 2 7 0 4.5 0z" fill="var(--brand-red)"/>
      <circle cx="4.5" cy="4.4" r="1.8" fill="#fff"/>
    </svg>
    Calder Row West<br>Brindlemoor, Ashworth<br>AB12 3CD
  </address>

  <section class="recipient">
    <h1 class="recipient-name">MARA QUILL</h1>
    <p>0123-456-789</p>
    <p>info@youremailaddress.com</p>
    <p class="recipient-address">1234 City Your Ln. Suite<br>123 Dallas, TX 0000</p>
  </section>

  <time class="letter-date" datetime="2023-12-12">12 December, 2023</time>

  <section class="letter-body">
    <p>Lorem ipsum dolor sit amet, consectetuer adipiscing elit, sed diam nonummy nibh euismod tincidunt ut laoreet dolore magna aliquam erat volutpat. Ut wisi enim ad minim veniam, quis nostrud exerci tation ullamcorper suscipit lobortis nisl ut aliquip ex ea commodo consequat. Duis autem vel eum iriure dolor in hendrerit in vulputate velit esse molestie consequat, vel illum dolore eu feugiat nulla facilisis at vero eros et accumsan et iusto odio dignissim qui blandit praesent luptatum zzril delenit augue duis dolore te feugait nulla facilisi.</p>
    <p>Lorem ipsum dolor sit amet, cons ectetuer adipiscing elit, sed diam nonummy nibh euismod tincidunt ut laoreet dolore magna aliquam erat volutpat. Ut wisi enim ad minim veniam, quis nostrud exerci tation ullamcorper suscipit lobortis nisl ut aliquip ex ea commodo consequat.</p>
    <p class="tight">Lorem ipsum dolor sit amet, consectetuer adipiscing elit, sed diam nonummy nibh euismod tincidunt ut laoreet dolore magna aliquam erat</p>
    <p class="spaced">Lorem ipsum dolor sit amet, cons ectetuer adipiscing elit, sed diam nonummy nibh euismod tincidunt ut laoreet dolore magna aliquam erat volutpat. Ut wisi enim ad minim veniam, quis nostrud exerci tation ullamcorper suscipit lobortis nisl ut aliquip ex ea commodo consequat. Lorem ipsum dolor sit zamet, consectetuer adipiscing elit, sed diam nonummy nibh euismod tincidunt.</p>
  </section>

  <p class="sign-off">Managing Director</p>
  <div class="handwritten-signature" role="img" aria-label="Handwritten signature of the managing director"></div>

  <ul class="letter-footer">
    <li>
      <svg class="contact-icon" width="8" height="8" viewBox="0 0 8 8" aria-hidden="true"><circle cx="4" cy="4" r="4" fill="var(--brand-red)"/><path d="M2.6 2.1l.8-.2.5 1-.5.4c.3.6.7 1 1.3 1.3l.4-.5 1 .5-.2.8c-1.9-.1-3.2-1.4-3.3-3.3z" fill="#fff"/></svg>
      161 555 0182
    </li>
    <li>
      <svg class="contact-icon" width="8" height="8" viewBox="0 0 8 8" aria-hidden="true"><circle cx="4" cy="4" r="4" fill="var(--brand-red)"/><rect x="2.1" y="2.7" width="3.8" height="2.6" fill="#fff"/><path d="M2.1 2.7L4 4.2l1.9-1.5" stroke="var(--brand-red)" stroke-width=".5" fill="none"/></svg>
      info@dremlox.co
    </li>
    <li>
      <svg class="contact-icon" width="8" height="8" viewBox="0 0 8 8" aria-hidden="true"><circle cx="4" cy="4" r="4" fill="var(--brand-red)"/><circle cx="4" cy="4" r="2.1" stroke="#fff" stroke-width=".6" fill="none"/><path d="M1.9 4h4.2M4 1.9v4.2" stroke="#fff" stroke-width=".5"/></svg>
      www.dremlox.co.uk
    </li>
  </ul>
</article>

<article class="email-signature">
  <div class="brand"><span class="brand-mark"></span>Dremlox Hubs &amp; Bearings Ltd</div>

  <div class="sender">
    <h2 class="sender-name">Alan Brook</h2>
    <p class="sender-role">Manager</p>
  </div>

  <ul class="sender-contacts">
    <li>
      <svg class="contact-icon" width="6" height="6" viewBox="0 0 8 8" aria-hidden="true"><circle cx="4" cy="4" r="4" fill="var(--brand-red)"/><path d="M2.6 2.1l.8-.2.5 1-.5.4c.3.6.7 1 1.3 1.3l.4-.5 1 .5-.2.8c-1.9-.1-3.2-1.4-3.3-3.3z" fill="#fff"/></svg>
      161 555 0182
    </li>
    <li>
      <svg class="contact-icon" width="6" height="6" viewBox="0 0 8 8" aria-hidden="true"><circle cx="4" cy="4" r="4" fill="var(--brand-red)"/><rect x="2.1" y="2.7" width="3.8" height="2.6" fill="#fff"/></svg>
      info@dremlox.co
    </li>
    <li>
      <svg class="contact-icon" width="6" height="6" viewBox="0 0 8 8" aria-hidden="true"><circle cx="4" cy="4" r="4" fill="var(--brand-red)"/><circle cx="4" cy="4" r="2.1" stroke="#fff" stroke-width=".7" fill="none"/></svg>
      www.dremlox.co.uk
    </li>
  </ul>

  <address class="sender-address" style="font-style:normal">
    Calder Row West<br>Brindlemoor, Ashworth<br>AB12 3CD
  </address>

  <div class="social">
    <p class="social-title">Follow us</p>
    <ul class="social-links" aria-label="Social profiles">
      <li></li><li></li><li></li>
    </ul>
  </div>
</article>

</body>
</html>
```